Need wine label for brand that is named: Casmerel Vineyards & Winery

Casmerel is a yoga way of breathing. In Sanskrit Casmerel means "flying up." I would like a creative wine label that articulates Casmerel. The label should include a graphic and the name Casmerel on one line and Vineyards & Winery in smaller print underneath Casmerel.

```html
<!DOCTYPE html>
<html lang="en">
<head>
<meta charset="utf-8">
<title>Casmerel Pinot Noir 2014 Label</title>
<link href="https://fonts.googleapis.com/css2?family=Cormorant+SC:wght@500&family=Mulish:wght@300;400;700&display=swap" rel="stylesheet">
<style>
  :root {
    --paper: #ffffff;
    --panel: #f3f3f3;
    --gold: #b98a4e;
    --gold-light: #e2bf82;
    --gold-deep: #9c6f35;
    --ink: #3a3a3a;
  }
  html, body {
    margin: 0;
    padding: 0;
    overflow: hidden;
    background: var(--paper);
  }
  .label {
    position: relative;
    width: 943px;
    height: 1200px;
    overflow: hidden;
    background: var(--paper);
    font-family: "Mulish", sans-serif;
    color: var(--ink);
  }
  .side-panel {
    position: absolute;
    top: 0;
    width: 172px;
    height: 1200px;
    background: linear-gradient(180deg, #f6f6f6, var(--panel));
  }
  .side-panel--left { left: 0; }
  .side-panel--right { right: 0; }
  .gold-rule {
    position: absolute;
    top: 0;
    width: 6px;
    height: 1200px;
    background: var(--gold);
  }
  .gold-rule--left { left: 172px; }
  .gold-rule--right { left: 764px; }
  .ornament {
    position: absolute;
    top: 296px;
    width: 126px;
    height: 596px;
    background: radial-gradient(ellipse at center, var(--gold-light), var(--gold) 55%, var(--gold-deep));
  }
  .ornament--left {
    left: 24px;
    border-radius: 100% 0 0 100% / 50% 0 0 50%;
  }
  .ornament--right {
    left: 792px;
    border-radius: 0 100% 100% 0 / 0 50% 50% 0;
  }
  .rosette {
    position: absolute;
    left: 424px;
    top: 552px;
    width: 96px;
    height: 96px;
    border-radius: 50%;
    background: radial-gradient(circle, var(--gold-light), var(--gold) 60%, var(--gold-deep));
  }
  .centered {
    position: absolute;
    left: 178px;
    width: 586px;
    text-align: center;
    margin: 0;
  }
  .brand-name {
    top: 98px;
    font-size: 86px;
    font-weight: 700;
    line-height: 1;
    color: var(--gold);
    letter-spacing: 1px;
  }
  .brand-sub {
    top: 238px;
    font-family: "Cormorant SC", serif;
    font-weight: 500;
    font-size: 27px;
    letter-spacing: 4px;
    line-height: 1;
  }
  .varietal {
    top: 376px;
    font-size: 74px;
    font-weight: 400;
    line-height: 1;
  }
  .vintage {
    top: 752px;
    font-size: 44px;
    font-weight: 700;
    letter-spacing: 8px;
    line-height: 1;
  }
  .collection {
    top: 840px;
    font-size: 46px;
    font-weight: 300;
    letter-spacing: 10px;
    line-height: 1;
    padding-left: 10px;
  }
  .region {
    top: 936px;
    font-size: 33px;
    font-weight: 700;
    line-height: 1;
  }
  .abv {
    top: 1154px;
    font-size: 21px;
    font-weight: 400;
    letter-spacing: 3px;
    line-height: 1;
  }
</style>
</head>
<body>
  <main class="label">
    <div class="side-panel side-panel--left" role="img" aria-label="Faint light grey paisley pattern"></div>
    <div class="side-panel side-panel--right" role="img" aria-label="Faint light grey paisley pattern"></div>
    <div class="gold-rule gold-rule--left"></div>
    <div class="gold-rule gold-rule--right"></div>

    <div class="ornament ornament--left" role="img" aria-label="Gold half-mandala ornament"></div>
    <div class="ornament ornament--right" role="img" aria-label="Gold half-mandala ornament"></div>

    <h1 class="centered brand-name">Casmerel</h1>
    <p class="centered brand-sub">Vineyards &amp; Winery</p>

    <h2 class="centered varietal">Pinot Noir</h2>

    <div class="rosette" role="img" aria-label="Small gold rosette ornament"></div>

    <p class="centered vintage">2014</p>
    <p class="centered collection">COLLECTION</p>
    <p class="centered region">Napa Valley</p>
    <p class="centered abv">11.8% alc/vol.</p>
  </main>
</body>
</html>
```